New Print Material Needed for Renovation Company

We are looking to update our current Print Material to reflect the current process we offer to our clients. A lot of the information is also outdated along with many of the photos that are currently being used. We are a renovation company that specializes in residential and commercial renovations and custom builds.This project is MULTIPLE pages. We will pay the chosen designer an extra fee for the designing 3-4 additional pages that are similar to the chosen design. Attached is our current Print Material. We are hoping to update the look of them and some of the messaging. Our current company colors are white, blue and light grey and it will remain that way.

Industry/Entity Type

Construction Company

Font styles to use
Sans Serif

Colors
3176b5
ffffff

Requirements
Must have
• Easy to explain the process
• Easy to read and understand let alone
• Easy to navigate
Nice to have
• As much creativity as possible
Should not have
• no confusing text
• no confusing layout

```html
<!DOCTYPE html>
<html lang="en">
<head>
<meta charset="utf-8">
<title>Master Builder Timeline</title>
<link rel="stylesheet" href="https://fonts.googleapis.com/css2?family=Open+Sans:wght@400;600;700;800&display=swap">
<style>
  :root {
    --brand-blue: #1a64a6;
    --deep-blue: #175b98;
    --title-blue: #1c5c96;
    --weeks-blue: #6e9dd0;
    --pale-blue: #dde6f1;
    --ink: #1b1b1b;
    --shadow-grey: #9c9c9c;
    --dot-grey: #a8a8a8;
    --white: #ffffff;
  }
  * { box-sizing: border-box; margin: 0; padding: 0; }
  html, body { width: 1200px; height: 1000px; overflow: hidden; background: var(--white); }
  body { font-family: "Open Sans", Arial, sans-serif; position: relative; }

  .sheet {
    position: absolute; left: 228px; top: 15px; width: 745px; height: 971px;
    border: 2px solid var(--brand-blue); background: var(--white); overflow: hidden;
  }
  .badge { position: absolute; left: 310px; top: 14px; }
  .ribbon-end { position: absolute; top: 136px; width: 26px; height: 46px; background: var(--brand-blue); }
  .ribbon-end.left { left: 17px; clip-path: polygon(0 0, 100% 0, 100% 100%, 0 100%, 45% 50%); }
  .ribbon-end.right { right: 17px; clip-path: polygon(0 0, 100% 0, 55% 50%, 100% 100%, 0 100%); }
  .headline {
    position: absolute; left: 0; right: 0; top: 128px; text-align: center;
    font-weight: 800; font-size: 44px; letter-spacing: 0.5px; color: #111;
  }

  .stage-column { position: absolute; left: 0; top: 192px; width: 297px; height: 780px; background: var(--brand-blue); }
  .edge-band { position: absolute; left: 707px; top: 208px; width: 38px; height: 700px; background: var(--deep-blue); }
  .footer-block { position: absolute; left: 372px; top: 862px; width: 373px; height: 110px; background: var(--deep-blue); }

  .stage-label {
    position: absolute; left: 20px; width: 36px; writing-mode: vertical-rl;
    color: var(--white); font-weight: 700; font-size: 27px; letter-spacing: 15px;
  }

  .stage-group { position: absolute; left: 57px; width: 238px; background: var(--pale-blue); }
  .step-item { position: absolute; left: 8px; right: 8px; }
  .step-name { font-weight: 700; font-size: 15.5px; line-height: 16px; color: var(--title-blue); letter-spacing: 0.2px; }
  .step-weeks { font-size: 12.5px; color: var(--weeks-blue); margin-top: 7px; }
  .step-note { height: 19px; background: var(--white); margin-top: 6px; }

  .connectors { position: absolute; left: 0; top: 0; }

  .step-card {
    position: absolute; left: 374px; width: 326px; height: 65px; background: var(--white);
    border: 1.5px solid var(--brand-blue); box-shadow: 7px 6px 0 var(--shadow-grey);
    padding: 6px 10px 0 28px; font-size: 14.5px; line-height: 16px; color: var(--ink);
  }
  .step-number {
    position: absolute; left: 348px; width: 44px; height: 44px; border-radius: 50%;
    background: var(--brand-blue); border: 3px solid var(--white); box-shadow: 0 0 0 1.5px var(--brand-blue);
    color: var(--white); font-weight: 700; font-size: 22px; line-height: 38px; text-align: center; z-index: 2;
  }

  .company-mark { position: absolute; left: 466px; top: 890px; display: flex; align-items: center; gap: 12px; }
  .company-dot { width: 40px; height: 40px; border-radius: 50%; border: 3px solid var(--white); }
  .company-name { color: var(--white); font-size: 16px; line-height: 19px; font-weight: 400; }
</style>
</head>
<body>
<div class="sheet">
  <svg class="badge" width="124" height="124" viewBox="0 0 124 124" role="img" aria-label="Builder tools seal badge">
    <circle cx="62" cy="62" r="60" fill="#1a64a6"/>
    <circle cx="62" cy="62" r="46" fill="none" stroke="#ffffff" stroke-width="3"/>
  </svg>
  <div class="ribbon-end left"></div>
  <div class="ribbon-end right"></div>
  <h1 class="headline">MASTER BUILDER TIMELINE</h1>

  <div class="stage-column"></div>
  <div class="edge-band"></div>
  <div class="footer-block"></div>

  <div class="stage-label" style="top:215px">DESIGN</div>
  <div class="stage-label" style="top:490px">PLAN</div>
  <div class="stage-label" style="top:722px">BUILD</div>

  <div class="stage-group" style="top:203px;height:230px">
    <div class="step-item" style="top:8px"><div class="step-name">INITIAL DESIGN MEETING</div><div class="step-weeks">1-2 WEEKS</div><div class="step-note"></div></div>
    <div class="step-item" style="top:78px"><div class="step-name">SECOND DESIGN MEETING</div><div class="step-weeks">1-2 WEEKS</div><div class="step-note"></div></div>
    <div class="step-item" style="top:148px"><div class="step-name">FINAL DESIGN<br>(PLAN + SCOPE)</div><div class="step-weeks">1-3 WEEKS</div><div class="step-note"></div></div>
  </div>
  <div class="stage-group" style="top:445px;height:228px">
    <div class="step-item" style="top:8px"><div class="step-name">MATERIAL SELECTION</div><div class="step-weeks">1-4 WEEKS</div><div class="step-note"></div></div>
    <div class="step-item" style="top:78px"><div class="step-name">ENGINEER DRAWINGS</div><div class="step-weeks">2-4 WEEKS</div><div class="step-note"></div></div>
    <div class="step-item" style="top:147px"><div class="step-name">COMPLETE BUILDING<br>PERMIT PLANS</div><div class="step-weeks">3-25 WEEKS</div><div class="step-note"></div></div>
  </div>
  <div class="stage-group" style="top:685px;height:240px">
    <div class="step-item" style="top:8px"><div class="step-name">FINALIZATION OF<br>MATERIALS</div><div class="step-weeks">2-4 WEEKS</div><div class="step-note"></div></div>
    <div class="step-item" style="top:93px"><div class="step-name">FINAL DOCS +<br>CONSTRUCTION PLANS</div><div class="step-weeks">2-6 WEEKS</div><div class="step-note"></div></div>
    <div class="step-item" style="top:176px"><div class="step-name">SCHEDULING</div><div class="step-weeks">2-4 WEEKS</div><div class="step-note"></div></div>
  </div>

  <svg class="connectors" width="745" height="971" viewBox="0 0 745 971" aria-hidden="true">
    <g fill="none" stroke="#a8a8a8" stroke-width="2.5" stroke-dasharray="2 3">
      <polyline points="295,236 350,236"/>
      <polyline points="295,300 342,300 342,308 350,308"/>
      <polyline points="295,386 337,386 337,374 350,374"/>
      <polyline points="295,474 337,474 337,446 350,446"/>
      <polyline points="295,538 337,538 337,530 350,530"/>
      <polyline points="295,624 337,624 337,596 350,596"/>
      <polyline points="295,724 320,724 320,672 350,672"/>
      <polyline points="295,814 317,814 317,746 350,746"/>
      <polyline points="295,880 340,880 340,822 350,822"/>
    </g>
  </svg>

  <div class="step-card" style="top:205px">The first step of the design process is to confirm the design concept you have envisioned.</div>
  <div class="step-number" style="top:214px">1</div>
  <div class="step-card" style="top:277px">Our designers work directly with you to ensure the measurements line up with your design ideas.</div>
  <div class="step-number" style="top:287px">2</div>
  <div class="step-card" style="top:351px">Any last minute or final revisions will be completed within three days of this meeting.</div>
  <div class="step-number" style="top:361px">3</div>
  <div class="step-card" style="top:425px">Our material selection coordinator will work with you to ensure all the right materials.</div>
  <div class="step-number" style="top:434px">4</div>
  <div class="step-card" style="top:498px">The final permit drawings will be sent to engineers to ensure structural integrity.</div>
  <div class="step-number" style="top:508px">5</div>
  <div class="step-card" style="top:571px">Permit drawings will begin once the build has been signed and initial payments have been made.</div>
  <div class="step-number" style="top:581px">6</div>
  <div class="step-card" style="top:645px">A lead designer will finalized any revisions you may have for your material section.</div>
  <div class="step-number" style="top:654px">7</div>
  <div class="step-card" style="top:718px">The drawings will be updated within 24 hours once the permits have been approved &amp; recived.</div>
  <div class="step-number" style="top:728px">8</div>
  <div class="step-card" style="top:792px">All designs, dates, permits have been completed. The project is ready to get underway.</div>
  <div class="step-number" style="top:801px">9</div>

  <div class="company-mark">
    <div class="company-dot"></div>
    <div class="company-name">Harbourline<br>General<br>Contractors</div>
  </div>
</div>
</body>
</html>
```